missions focus sunday

i am a christian who is tasked to do a simple presentation of missions work in northern germany. i have some ideas which i have sketched out as enclosed.
can you do the postcard in black background with words/diagrams in white? thanks

Industry/Entity Type

Christian

```html
<!DOCTYPE html>
<html lang="en">
<head>
<meta charset="utf-8">
<title>Missions Focus Sunday – Postcard</title>
<link rel="stylesheet" href="https://fonts.googleapis.com/css2?family=Dancing+Script:wght@500;700&family=Kaushan+Script&display=swap">
<style>
  :root {
    --ink: #000000;
    --paper: #ffffff;
    --stage: #eeeeee;
    --cloud-shade: #d9d9d9;
    --skyline-top: #1a1a1a;
    --skyline-bottom: #5a5a5a;
    --emblem-tone: #bfbfbf;
  }
  * { margin: 0; padding: 0; box-sizing: border-box; }
  html, body { width: 946px; height: 1200px; overflow: hidden; }
  body { background: var(--stage); position: relative; font-family: "Dancing Script", cursive; }

  /* ---------- Front of postcard ---------- */
  .postcard-front {
    position: absolute; left: 65px; top: 49px;
    width: 660px; height: 510px;
    background: var(--paper); padding: 16px;
  }
  .front-panel {
    position: relative; width: 100%; height: 100%;
    background: var(--ink); overflow: hidden; color: var(--paper);
  }
  .route-lines { position: absolute; inset: 0; width: 100%; height: 100%; }

  .caption {
    position: absolute; font-family: "Kaushan Script", cursive;
    font-size: 17px; line-height: 1.35; color: var(--paper);
  }
  .caption-power { left: 18px; top: 78px; }
  .caption-power .indent { padding-left: 28px; display: block; }
  .caption-calling { right: 22px; top: 378px; text-align: right; }
  .caption-calling .indent { padding-right: 0; display: block; }

  .art {
    position: absolute;
  }
  .art-footsteps { left: 100px; top: 114px; width: 80px; height: 46px;
    background: radial-gradient(ellipse at center, #ffffff 0%, #cfcfcf 70%, transparent 72%); }
  .art-emblem { left: 490px; top: 42px; width: 44px; height: 64px;
    background: linear-gradient(#ffffff, var(--emblem-tone)); border-radius: 4px 4px 22px 22px; }
  .art-plane { left: 420px; top: 303px; width: 68px; height: 64px;
    background: linear-gradient(135deg, transparent 30%, #e6e6e6 30%, #bdbdbd 70%, transparent 70%); }
  .art-skyline { left: 0; right: 0; bottom: 0; height: 98px;
    background: linear-gradient(var(--skyline-top), var(--skyline-bottom)); opacity: 0.85; }

  .tower-frame {
    position: absolute; left: 63px; top: 338px; width: 85px; height: 85px;
    border: 2px solid var(--paper); border-radius: 10px; background: var(--ink);
    padding: 8px;
  }
  .art-tower { position: static; width: 100%; height: 100%;
    background: linear-gradient(#ffffff, #9a9a9a); border-radius: 4px; }

  .dream-cloud { position: absolute; left: 188px; top: 168px; width: 244px; height: 138px; }
  .dream-cloud svg { position: absolute; inset: 0; width: 100%; height: 100%; }
  .dream-text {
    position: absolute; inset: 0; display: flex; align-items: center; justify-content: center;
    text-align: center; color: var(--ink); font-size: 21px; font-weight: 500; line-height: 1.35;
    font-style: italic; padding-top: 4px;
  }

  /* ---------- Back of postcard ---------- */
  .postcard-back {
    position: absolute; left: 223px; top: 595px;
    width: 657px; height: 504px;
    background: var(--ink); padding: 19px;
  }
  .back-panel { position: relative; width: 100%; height: 100%; background: var(--paper); }
  .hope-quote {
    position: absolute; right: 26px; bottom: 46px;
    font-family: "Kaushan Script", cursive; font-size: 10.5px; color: var(--ink);
  }
  .quote-author {
    position: absolute; right: 30px; bottom: 22px;
    font-family: "Kaushan Script", cursive; font-size: 13px; color: var(--ink);
  }
</style>
</head>
<body>

<section class="postcard-front" aria-label="Postcard front">
  <div class="front-panel">
    <div class="art art-skyline" role="img" aria-label="White city skyline silhouette along the bottom edge"></div>

    <svg class="route-lines" viewBox="0 0 628 478" aria-hidden="true">
      <g fill="none" stroke="#ffffff" stroke-width="1.4" stroke-dasharray="1.5 4" stroke-linecap="round">
        <path d="M66 305 Q 95 60 402 55"/>
        <path d="M548 170 Q 540 405 200 415"/>
      </g>
      <g fill="#cfcfcf">
        <path d="M414 55 L400 49 L403 55 L400 61 Z"/>
        <path d="M188 415 L202 409 L199 415 L202 421 Z"/>
      </g>
    </svg>

    <p class="caption caption-power">the power<span class="indent">of 2</span></p>
    <div class="art art-footsteps" role="img" aria-label="Two white footprints"></div>

    <div class="art art-emblem" role="img" aria-label="National coat of arms emblem of Germany"></div>

    <div class="dream-cloud">
      <svg viewBox="0 0 244 138" aria-hidden="true">
        <defs>
          <radialGradient id="cloudFill" cx="50%" cy="45%" r="60%">
            <stop offset="0%" stop-color="#ffffff"/>
            <stop offset="80%" stop-color="#f2f2f2"/>
            <stop offset="100%" stop-color="#d9d9d9"/>
          </radialGradient>
        </defs>
        <path fill="url(#cloudFill)" stroke="#ffffff" stroke-width="2"
          d="M40 112 C 12 112 6 80 28 70 C 18 46 46 30 66 40 C 72 14 110 6 126 28 C 140 8 180 14 182 40 C 210 34 236 54 222 78 C 242 92 228 122 200 116 C 188 134 156 134 146 120 C 130 136 96 134 88 120 C 72 132 44 128 40 112 Z"/>
      </svg>
      <p class="dream-text">Last night I<br>dream of this</p>
    </div>

    <div class="art art-plane" role="img" aria-label="White airplane in flight"></div>

    <p class="caption caption-calling">answering<span class="indent">the “come” call</span></p>

    <div class="tower-frame">
      <div class="art art-tower" role="img" aria-label="Airport control tower"></div>
    </div>
  </div>
</section>

<section class="postcard-back" aria-label="Postcard back">
  <div class="back-panel">
    <p class="hope-quote">everything that is done in the world is done by hope.</p>
    <p class="quote-author">Marten Lowe</p>
  </div>
</section>

</body>
</html>
```